MoveNest Landing Page

We need to freshen up our homepage.

The company is MoveNest.com. We provide cloud-based management software for class venues - dance, yoga, martial arts, etc.

The challenge here is to create something that's simultaneously lighthearted and professional. We want our customers to know that the software is easy, fun and non-intimidating, but also powerful enough to handle whatever they throw at it.

Page content can remain the same as it is now. Feel free to move things around, manipulate it however you like.

We like our logo, but feel free to manipulate it as part of your design. Fonts used in the logo are Futura Extra Bold and Rockwell.

NOTE: The default screenshot in the homepage video is NOT our branding choice, it just happens to be the default freeze frame from vidloop.. Feel free to ignore it altogether in your design. We are not affiliated with that character, or the app that we used to create the vid.
Updates

Project Deadline Extended
Reason: We are extending this contest by request. Out of 65 designs, so far we only really like 4. There's still a good chance to win this contract! Please submit your very best :) Owen

Target Market(s)

Studio owners who are not necessarily tech savvy.

Industry/Entity Type

Software

Requirements
Must have
• Look and feel of a modern web app.

Delivery in a layered PSD.

```html
<!DOCTYPE html>
<html lang="en">
<head>
<meta charset="utf-8">
<title>MoveNest – The easiest way to manage your classes</title>
<link href="https://fonts.googleapis.com/css2?family=Open+Sans:ital,wght@0,400;0,600;0,700;0,800;1,400&family=Roboto+Slab:wght@400;700;800;900&family=Jost:wght@800&display=swap" rel="stylesheet">
<style>
:root{
  --blue:#2763b6;
  --blue-dark:#1a4a8d;
  --blue-deep:#123c78;
  --green:#7ae014;
  --green-dark:#5fb50c;
  --green-box:#7ce611;
  --green-card:#6cc614;
  --orange:#fa5400;
  --orange-dark:#c64200;
  --paper:#f4f4f4;
  --grey-text:#8a8a8a;
  --title-blue:#4f79a8;
  --nav-text:#6b6b6b;
  --white:#ffffff;
}
*{margin:0;padding:0;box-sizing:border-box}
html,body{width:1200px;height:994px;overflow:hidden}
body{background:var(--paper);font-family:"Open Sans",sans-serif;position:relative}

.site-header{position:absolute;left:0;top:0;width:1200px;height:77px;background:var(--white)}
.brand{position:absolute;left:131px;top:17px;font-family:"Jost",sans-serif;font-weight:800;font-size:34px;color:var(--blue);letter-spacing:.5px;display:flex;align-items:center;gap:8px}
.brand-dot{width:12px;height:12px;border-radius:50%;background:var(--green)}
.main-nav{position:absolute;top:26px;left:625px;display:flex;gap:28px}
.main-nav a{display:flex;align-items:center;gap:8px;font-weight:700;font-size:16px;color:var(--nav-text);text-decoration:none;letter-spacing:.3px}
.main-nav svg{width:18px;height:18px}
.btn{display:flex;align-items:center;justify-content:center;gap:6px;color:var(--white);text-decoration:none;font-family:"Roboto Slab",serif;font-weight:800;border-radius:6px;white-space:nowrap}
.btn-orange{background:var(--orange);box-shadow:0 3px 0 var(--orange-dark)}
.btn-green{background:var(--green);box-shadow:0 3px 0 var(--green-dark)}
.btn-start{position:absolute;left:928px;top:17px;width:130px;height:41px;font-size:13px}

.hero{position:absolute;left:0;top:77px;width:1200px;height:350px;background:var(--blue)}
.hero-mark{position:absolute;left:135px;top:58px;width:335px;height:205px;display:flex;align-items:center;justify-content:center;gap:14px;border:8px solid var(--white);border-radius:100px;font-family:"Roboto Slab",serif;font-weight:900;font-size:46px;color:var(--white);white-space:nowrap}
.hero-mark-dot{width:26px;height:26px;border-radius:50%;background:var(--white)}
.hero-title{position:absolute;left:540px;top:70px;width:538px;text-align:center;color:var(--white);font-family:"Roboto Slab",serif;font-weight:900;text-transform:uppercase;line-height:1;white-space:nowrap}
.hero-title .lead{display:block;font-size:46px;letter-spacing:.5px}
.hero-title .line{display:block;font-size:28px;margin-top:6px}
.hero-title small{font-size:21px}
.hero-cta{position:absolute;top:203px;width:220px;height:64px;border-radius:6px}
.hero-cta .num{font-size:22px}
.hero-cta .label{display:block;font-size:13px;text-transform:uppercase;line-height:1.1}
.hero-cta .note{display:block;font-family:"Open Sans",sans-serif;font-style:italic;font-weight:400;font-size:13px;text-align:center}
.cta-video{left:550px}
.cta-setup{left:850px}
.hero-cta svg{position:absolute;left:14px;top:15px;width:34px;height:34px}
.hero-cta .text{position:absolute;left:60px;top:10px}
.hero-cta .chev{position:absolute;right:10px;top:22px;font-size:16px}

.features{position:absolute;left:121px;top:455px;display:flex}
.feature{width:160px;text-align:center}
.feature svg{width:72px;height:72px;display:block;margin:0 auto}
.feature h3{font-weight:600;font-size:18px;color:var(--title-blue);margin-top:9px;letter-spacing:.2px}
.feature p{font-size:14px;color:var(--grey-text);line-height:16px;margin:2px auto 0;max-width:150px}
.feature-versatile p{max-width:110px}
.btn-learn{position:absolute;left:523px;top:610px;width:152px;height:47px;font-size:14px}

.faq-box{position:absolute;top:719px;width:460px;height:160px;border-radius:6px;overflow:hidden}
.faq-q{left:129px;background:var(--blue);box-shadow:0 3px 0 var(--blue-deep)}
.faq-a{left:609px;background:var(--green-box);box-shadow:0 3px 0 var(--green-dark)}
.faq-letter{position:absolute;font-family:"Roboto Slab",serif;font-weight:900;font-size:120px;line-height:1}
.faq-q .faq-letter{left:26px;top:22px;color:var(--blue-deep)}
.faq-a .faq-letter{left:24px;top:22px;color:var(--green-dark)}
.faq-q h2{position:absolute;left:127px;top:32px;color:var(--white);font-family:"Roboto Slab",serif;font-weight:900;font-size:42px;line-height:48px;white-space:nowrap}
.faq-a p{position:absolute;left:130px;top:26px;width:310px;color:var(--white);font-size:14px;line-height:17px}

.plan{position:absolute;top:946px;width:300px;height:60px;border-radius:4px 4px 0 0;text-align:center;color:var(--white);font-family:"Roboto Slab",serif;font-size:34px;padding-top:8px}
.plan-standard{left:128px;background:var(--orange)}
.plan-premium{left:448px;background:var(--green-card)}
.plan-pro{left:767px;background:var(--blue)}
</style>
</head>
<body>

<header class="site-header">
  <div class="brand"><span>MoveNest</span><span class="brand-dot"></span></div>
  <nav class="main-nav">
    <a href="#"><svg viewBox="0 0 18 18"><path d="M9 2 1 9h2.5v7h4v-4h3v4h4V9H17z" fill="#5b9be6"/></svg>HOME</a>
    <a href="#"><svg viewBox="0 0 18 18"><circle cx="6" cy="6" r="4" fill="#5b9be6"/><path d="M8 8l8 8M13 13l2-2" stroke="#5b9be6" stroke-width="2.5"/></svg>LOGIN</a>
    <a href="#"><svg viewBox="0 0 18 18"><circle cx="9" cy="9" r="6.5" fill="none" stroke="#5b9be6" stroke-width="2.5"/><circle cx="9" cy="9" r="2.5" fill="none" stroke="#5b9be6" stroke-width="2"/></svg>HELP</a>
  </nav>
  <a href="#" class="btn btn-orange btn-start">GET STARTED ›</a>
</header>

<section class="hero">
  <div class="hero-mark" aria-label="MoveNest"><span class="hero-mark-dot"></span><span>MoveNest</span></div>
  <h1 class="hero-title">
    <span class="lead">The easiest way</span>
    <span class="line"><small>to</small> manage your classes</span>
    <span class="line"><small>and</small> accept payments online</span>
  </h1>
  <a href="#" class="btn btn-green hero-cta cta-video">
    <svg viewBox="0 0 34 34"><path d="M5 3 30 17 5 31z" fill="none" stroke="#fff" stroke-width="2.5" stroke-linejoin="round"/></svg>
    <span class="text"><span class="label"><span class="num">1</span> Minute video</span><span class="note">How it works</span></span>
    <span class="chev">›</span>
  </a>
  <a href="#" class="btn btn-orange hero-cta cta-setup">
    <svg viewBox="0 0 34 34"><path d="M3 31 20 14" stroke="#fff" stroke-width="3"/><path d="M24 3l2 5 5 1-4 3 1 5-4-3-4 3 1-5-4-3 5-1z" fill="none" stroke="#fff" stroke-width="2"/></svg>
    <span class="text"><span class="label"><span class="num">5</span> Minute setup!</span><span class="note">It's Free :)</span></span>
    <span class="chev">›</span>
  </a>
</section>

<section class="features">
  <div class="feature">
    <svg viewBox="0 0 72 72" fill="none" stroke="var(--green)" stroke-width="4"><rect x="6" y="12" width="60" height="40" rx="2"/><path d="M36 52v10M22 62h28"/></svg>
    <h3>WEB BASED</h3><p>Logn anywhere</p>
  </div>
  <div class="feature">
    <svg viewBox="0 0 72 72" fill="none" stroke="var(--green)" stroke-width="4" stroke-linejoin="round"><path d="M62 12 10 32l24 6 6 24z"/></svg>
    <h3>INTUITIVE</h3><p>Easy to use</p>
  </div>
  <div class="feature">
    <svg viewBox="0 0 72 72" fill="none" stroke="var(--green)" stroke-width="4" stroke-linejoin="round"><path d="M64 6c-18 0-32 10-40 30l12 12c20-8 30-22 28-42z"/><circle cx="46" cy="26" r="5"/><path d="M24 36H12l8-12h12M36 48v12l12-8V40M22 50c-6 2-10 8-12 14 6-2 12-6 14-12"/></svg>
    <h3>ROBUST</h3><p>Fast and powerful</p>
  </div>
  <div class="feature">
    <svg viewBox="0 0 72 72" fill="none" stroke="var(--green)" stroke-width="4"><rect x="12" y="30" width="48" height="34" rx="4"/><path d="M22 30v-8a14 14 0 0 1 28 0v8"/><circle cx="36" cy="44" r="3" fill="var(--green)"/><path d="M36 46v7"/></svg>
    <h3>SECURE</h3><p>Your info is super safe</p>
  </div>
  <div class="feature feature-versatile">
    <svg viewBox="0 0 72 72" fill="none" stroke="var(--green)" stroke-width="4"><path d="M10 10l16 16M10 10h12M10 10v12M62 10 46 26M62 10H50M62 10v12M10 62l16-16M10 62h12M10 62V50M62 62 46 46M62 62H50M62 62V50"/></svg>
    <h3>VERSATILE</h3><p>Suitable for any class venue</p>
  </div>
  <div class="feature">
    <svg viewBox="0 0 72 72" fill="none" stroke="var(--green)" stroke-width="4" stroke-linejoin="round"><rect x="8" y="24" width="56" height="12"/><rect x="12" y="36" width="48" height="28"/><path d="M36 24v40M36 24c-4-10-16-14-16-6 0 4 8 6 16 6 8 0 16-2 16-6 0-8-12-4-16 6"/></svg>
    <h3>AFFORDABLE</h3><p>Free version!</p>
  </div>
</section>
<a href="#" class="btn btn-orange btn-learn">LEARN MORE ›</a>

<section>
  <div class="faq-box faq-q">
    <span class="faq-letter">Q</span>
    <h2>What is<br>MoveNest?</h2>
  </div>
  <div class="faq-box faq-a">
    <span class="faq-letter">A</span>
    <p>MoveNest is the easiest and most affordable way to manage your class studio or venue. We help simplify your daily tasks by leveraging the power of the internet, saving you time and money. Anyone can learn to use MoveNest with our clean, common-sense website.</p>
  </div>
</section>

<section>
  <div class="plan plan-standard">Standard</div>
  <div class="plan plan-premium">Premium</div>
  <div class="plan plan-pro">Professional</div>
</section>

</body>
</html>
```